Traineeship Flyer Design Project

Requirements:
• 1 x A4 page flyer (double sided)
1st page; target market 15-19 yr old, looking for young/fresh, exciting, eye catching
2nd page: same look/feel – target market – parents/person to determine if there is value to devoting energy to this qualification (potentially less busy in design)
• Use of high quality logos: 1. Kestravo 2. Nationally recognised training logo
Ideally wanting to keep amount of copy to the page layout as attached, although designer is free to interpret the layout of copy on each page, although Kestravo will accept alternative presentation if designer sees new way to combine information
• Kestravo does not have a set colour palette so there are no restrictions/guidelines to follow
Updates
Hi, All files including brief and logos have now been updated.
Reason: Hi everyone
Please refer to design submission below for the only design that was deemed to cover off on the brief as the starting point - in regards to producing a design that appeals to target market of young person (15-19) in regards to self selecting to take up further study
Hi everyone
Can you please view the 3 remaining designs that are in contention (out of 30+ submitted) - Design 1528020 ; 1510098; 1510087; I will be providing additional feedback to these designers, as that come closer to the mark of appealing to younger "potential trainee" - the collateral needs to make the young student want to pick up the flyer (eye catching/interesting) and then be motivated to want to self elect - "beg parents" to take up the option. **PLEASE NOTE - I have uploaded a colour swatch now, and would appreciate if desgins could use these colours (not a requirement to use base colours of blue a silver as base if an exciting image needs to come from leaning on "secondary colours" (brighter) as being the predominant colours.
Many thanks, appreciate being able to see such an active community of designers involved in this website
Target Market(s)
1st page; target market 15-19 yr old, looking for young/fresh, exciting, eye catching. same look/feel – target market – parents/person to decide on
Industry/Entity Type
Training
Look and feel
Each slider illustrates characteristics of the customer's brand and the style your logo design should communicate.

```html
<!DOCTYPE html>
<html lang="en">
<head>
<meta charset="utf-8">
<title>Kestravo Traineeships</title>
<link rel="stylesheet" href="https://fonts.googleapis.com/css2?family=Archivo+Narrow:wght@400;600;700&family=Arimo:wght@400;700&display=swap">
<style>
:root{
  --cream:#f4ece0;
  --tan:#dcc6a8;
  --band:#c9ad8a;
  --charcoal:#3a3836;
  --ink:#1c1a18;
  --orange:#e8772b;
  --footer-text:#cfcac2;
}
*{margin:0;padding:0;box-sizing:border-box}
html,body{width:848px;height:1200px;overflow:hidden;background:var(--cream)}
.flyer{position:relative;width:848px;height:1200px;background:var(--cream);color:var(--ink);font-family:"Arimo",Arial,sans-serif;overflow:hidden}
.map-backdrop{position:absolute;left:0;top:23px;width:100%;height:1138px;
  background:linear-gradient(160deg,var(--tan) 0%,var(--cream) 45%,var(--tan) 100%);opacity:.7}
.top-bar{position:absolute;left:0;top:0;width:100%;height:10px;background:var(--charcoal)}
.top-band{position:absolute;left:0;top:10px;width:100%;height:13px;background:var(--band)}
.abs{position:absolute;white-space:nowrap}
.heading{font-family:"Archivo Narrow","Arial Narrow",sans-serif;font-weight:700;color:var(--orange);font-size:27px;line-height:30px}
.heading .num{color:var(--ink)}
.reasons{font-family:"Archivo Narrow","Arial Narrow",sans-serif;font-weight:600;font-size:17.5px;line-height:20px}
.reasons .n{color:var(--orange);position:absolute;left:51px}
.reasons .t{position:absolute;left:103px}
.topics{font-family:"Archivo Narrow","Arial Narrow",sans-serif;font-weight:600;font-size:17.7px;line-height:20px}
.topics span::before{content:"";position:absolute;left:-25px;top:8px;width:5px;height:5px;border-radius:50%;background:var(--ink)}
.careers-label{font-family:"Archivo Narrow","Arial Narrow",sans-serif;font-weight:700;font-size:18.3px;line-height:22px}
.career{font-family:"Archivo Narrow","Arial Narrow",sans-serif;font-weight:600;font-size:17.5px;line-height:20px}
.info-frame{position:absolute;left:0;top:0}
.sub{font-family:"Archivo Narrow","Arial Narrow",sans-serif;font-weight:700;color:var(--orange);font-size:27px;line-height:31px}
.para{font-size:15.2px;line-height:20px}
.quote{font-family:"Archivo Narrow","Arial Narrow",sans-serif;font-weight:600;font-size:17.9px;line-height:22px}
.quote::before{content:"";position:absolute;left:-23px;top:9px;width:5px;height:5px;border-radius:50%;background:var(--ink)}
.footer{position:absolute;left:0;bottom:0;width:100%;height:39px;background:var(--ink)}
.footer span{position:absolute;top:13px;font-size:9.5px;color:var(--footer-text);letter-spacing:.5px}
</style>
</head>
<body>
<div class="flyer">
  <div class="map-backdrop" role="img" aria-label="Faint world map decoration in warm tan tones"></div>
  <div class="top-bar"></div>
  <div class="top-band"></div>

  <div class="abs heading" style="left:51px;top:49px"><span class="num">5</span> Great reasons to complete a Traineeship</div>
  <div class="reasons">
    <div class="abs" style="top:87px;left:0;width:848px"><span class="n">1.</span><span class="t">It’s a formal qualification | Recognised nationally | Equivalent to attending TAFE</span></div>
    <div class="abs" style="top:108px;left:0;width:848px"><span class="n">2.</span><span class="t">Supercharge your resume, stand out from the crowd</span></div>
    <div class="abs" style="top:130px;left:0;width:848px"><span class="n">3.</span><span class="t">No formal ‘exams’: complete workbooks, online and practical tasks instead</span></div>
    <div class="abs" style="top:150px;left:0;width:848px"><span class="n">4.</span><span class="t">Learn new skills with people you work with, in the comfort of your workplace</span></div>
    <div class="abs" style="top:170px;left:0;width:848px"><span class="n">5.</span><span class="t">Earn while you learn</span></div>
  </div>

  <div class="abs heading" style="left:51px;top:244px">Topics covered in your qualification which teach transferable skills<br>may include;</div>
  <div class="topics">
    <span class="abs" style="left:77px;top:312px">Customer service</span>
    <span class="abs" style="left:77px;top:333px">Teamwork/communication</span>
    <span class="abs" style="left:77px;top:353px">Safety/security</span>
    <span class="abs" style="left:77px;top:373px">Marketing</span>
    <span class="abs" style="left:77px;top:395px">Food safety</span>
    <span class="abs" style="left:499px;top:312px">Merchandising</span>
    <span class="abs" style="left:499px;top:333px">Finance</span>
    <span class="abs" style="left:499px;top:353px">Manage sales and service</span>
    <span class="abs" style="left:499px;top:373px">Goal setting</span>
  </div>

  <div class="abs careers-label" style="left:51px;top:496px">Excellent possible career choices</div>
  <svg class="abs" style="left:296px;top:437px" width="30" height="146" viewBox="0 0 30 146">
    <path d="M6 2 Q18 2 18 14 L18 58 Q18 72 28 73 Q18 74 18 88 L18 132 Q18 144 6 144" fill="none" stroke="var(--ink)" stroke-width="3"/>
  </svg>
  <div class="career">
    <span class="abs" style="left:348px;top:445px">Senior sales assistant</span>
    <span class="abs" style="left:348px;top:465px">Office Administrator</span>
    <span class="abs" style="left:348px;top:486px">Accounts Clerk</span>
    <span class="abs" style="left:348px;top:506px">Merchandise manager</span>
    <span class="abs" style="left:348px;top:527px">Customer service manager</span>
    <span class="abs" style="left:348px;top:547px">Small business retail owner</span>
  </div>

  <svg class="info-frame" width="848" height="1200" viewBox="0 0 848 1200">
    <path d="M26 628 L326 628 L358 591 L825 591 L825 989 L26 989 Z" fill="none" stroke="var(--ink)" stroke-width="1.4"/>
  </svg>

  <div class="abs sub" style="left:33px;top:643px">What if I am at school?</div>
  <div class="abs para" style="left:33px;top:681px">School based Traineeships provide credit towards your secondary school certificate. Schools and employers will<br>work together to provide you with the best options.</div>
  <div class="abs sub" style="left:33px;top:726px">Am I eligible?</div>
  <div class="abs para" style="left:33px;top:765px">The government has strict criteria for Traineeships, which varies in each state. Submit your expression of interest<br>and your application will be reviewed to determine your eligibility.</div>
  <div class="abs sub" style="left:33px;top:810px">Who provides the training?</div>
  <div class="abs para" style="left:33px;top:851px;line-height:20.5px">Kestravo is an award winning national registered training organisation with over 14 years experience.<br>Kestravo encourages participation of learners with physical or mental disabilities in supporting the Equal<br>Opportunity Act 1995 and other laws. Government Funding is also available in some states for this program.<br>If you have any further questions about Traineeships, please contact your local Kestravo Training office on the<br>details below.</div>

  <div class="abs quote" style="left:94px;top:1014px">“The role plays in the course were great, now I am much more confident about handling customers”</div>
  <div class="abs quote" style="left:94px;top:1048px">“I was a bit worried it would be hard to do, but my Trainer made sure we were all OK”</div>
  <div class="abs quote" style="left:94px;top:1082px">“I learnt so much and just got promoted to a management role this year. Everyone is happy for me”</div>

  <div class="footer">
    <span style="left:71px">W &nbsp;: &nbsp;www.kestravo.com.au</span>
    <span style="left:306px">T &nbsp;: &nbsp;1300555018</span>
    <span style="left:442px">E &nbsp;: &nbsp;info@kestravo.com.au</span>
    <span style="left:675px">RTO &nbsp;ID &nbsp;: &nbsp;4107</span>
  </div>
</div>
</body>
</html>
```